Fiscal Sponsorship Program Flyer

We are seeking a designer to create a 1-2 flyer that explains our fiscal sponsorship program. This flyer will be used to recruit new projects that might be interested in utilizing our fiscal sponsorship services. The pertinent information about our program can be found in the attached PDF. For users who cannot access the PDF, please try this link: https://files.brivanto.net/slides/d/7QtR2wXkLmZp9HvCs4YdNe8JfGaUoBi3Tx5Wl0KyRc2s/view?mode=shared

Target Market(s)

New charitable projects that do not yet have their own 501(c)(3) status, and are seeking a fiscal sponsor.

Industry/Entity Type

Nonprofit/Charity

Requirements
Must have
• The flyer must include the language and detail included on the attached PDF. The desire is to reformat this to be more appealing and easy to read.

```html
<!DOCTYPE html>
<html lang="en">
<head>
<meta charset="utf-8">
<title>Meridian Foundation – Fiscal Sponsorship Program</title>
<link href="https://fonts.googleapis.com/css2?family=Playfair+Display:wght@700;900&family=Montserrat:wght@400;500;600;700;800&display=swap" rel="stylesheet">
<style>
:root{
  --backdrop:#ece8ee;
  --paper:#ffffff;
  --mint:#b3e5df;
  --mint-soft:#c6ece6;
  --coral:#f45f5f;
  --coral-deep:#e04a4a;
  --ink:#161616;
  --text:#2b2b2b;
  --white:#ffffff;
  --rule:#9a9a9a;
}
*{margin:0;padding:0;box-sizing:border-box}
html,body{width:1200px;height:2657px;overflow:hidden;background:var(--backdrop)}
body{font-family:"Montserrat",Arial,sans-serif;color:var(--text);letter-spacing:-0.025em}
.stage{position:absolute;left:0;top:0;width:1164px;height:2576px;transform:scale(1.0309);transform-origin:0 0}
.page{position:absolute;left:185px;width:794px;background:var(--paper);overflow:hidden}
.page--intro{top:213px;height:1027px}
.page--details{top:1347px;height:1028px}
.abs{position:absolute}

/* intro header */
.hero{left:0;top:0;width:794px;height:340px;background:var(--mint)}
.hero__name{left:55px;top:42px;font-family:"Playfair Display",Georgia,serif;font-weight:900;font-size:82px;line-height:76px;color:var(--ink);letter-spacing:-0.5px;white-space:nowrap}
.hero__rule{left:55px;top:198px;width:91px;height:5px;background:var(--coral)}
.hero__program{left:55px;top:218px;font-family:"Playfair Display",Georgia,serif;font-weight:900;font-size:50px;line-height:48px;color:var(--coral);letter-spacing:0;white-space:nowrap}

.section-title{font-family:"Playfair Display",Georgia,serif;font-weight:900;color:var(--coral);padding-left:17px;border-left:5px solid var(--coral);line-height:1;letter-spacing:0;white-space:nowrap}
.section-title--sm{font-size:27px;line-height:27px}
.para{font-size:13px;line-height:16px;color:var(--text)}
.para + .para{margin-top:15px}
.subhead{font-size:15.5px;line-height:21px;font-weight:600;color:var(--coral)}

.criteria{list-style:none}
.criteria li{position:relative;padding-left:25px;font-size:12.6px;line-height:16px;font-weight:700;color:var(--ink);margin-bottom:5px}
.criteria li span{position:absolute;left:0;top:1px;width:16px;height:16px;border-radius:50%;background:var(--coral);color:var(--white);font-size:10px;line-height:16px;text-align:center;font-weight:700}

.philosophy{left:448px;top:532px;width:292px;height:406px;background:var(--coral);border:1px solid var(--coral-deep);border-radius:24px 24px 0 24px;padding:24px 18px 0 24px}
.philosophy__title{font-family:"Playfair Display",Georgia,serif;font-weight:900;font-size:23px;line-height:30px;color:var(--ink);border-left:4px solid var(--white);padding-left:10px;margin-bottom:24px;white-space:nowrap;letter-spacing:-0.2px}
.philosophy p{font-size:12.2px;line-height:15.7px;font-weight:600;color:var(--white);letter-spacing:-0.03em}
.philosophy p + p{margin-top:16px}

.contact{left:0;width:794px;display:flex;justify-content:center;gap:22px;font-size:15.5px;color:var(--text);letter-spacing:0}
.contact__item{display:flex;align-items:center;gap:9px}

/* details page */
.values-band{left:0;top:0;width:794px;height:310px;background:var(--coral)}
.section-title--lg{font-size:34px;line-height:34px}
.section-title--commit{font-size:31px;line-height:34px}
.section-title--light{color:var(--white);border-left-color:var(--white)}
.value{display:flex;gap:11px;width:350px}
.value__icon{flex:none;width:44px;height:44px;border-radius:50%;background:var(--white);border:3px solid var(--coral);box-shadow:0 0 0 2px var(--white);display:flex;align-items:center;justify-content:center}
.value__label{font-size:11px;font-weight:700;color:var(--ink);line-height:13px}
.value__text{font-size:11px;line-height:14px;color:var(--white)}

.commit-col{display:flex;flex-direction:column;gap:14px}
.commit{display:flex;gap:22px}
.commit__tick{flex:none;margin-top:-3px}
.commit__text{font-size:11.5px;line-height:14px;font-weight:600;color:var(--ink)}

.divider{left:55px;top:545px;width:683px;height:1px;background:var(--rule)}
.fee-title{left:0;top:555px;width:794px;text-align:center;font-family:"Playfair Display",Georgia,serif;font-weight:900;font-size:34px;color:var(--ink);letter-spacing:0}
.fee-title em{font-style:normal;color:var(--coral)}

.tier{top:608px;width:214px;height:336px;background:var(--white);border:1px solid #e3e3e3;border-radius:14px;box-shadow:0 3px 8px rgba(0,0,0,.14);overflow:hidden}
.tier__banner{position:absolute;left:0;top:0}
.tier__name{position:absolute;left:0;top:20px;width:100%;text-align:center;font-weight:800;font-size:19.5px;line-height:23px;color:var(--ink);letter-spacing:0}
.tier__level{position:absolute;left:30px;top:110px;font-weight:800;font-size:18.5px;color:var(--coral);letter-spacing:0;white-space:nowrap}
.tier__body{position:absolute;left:28px;top:140px;width:180px}
.tier__lead{font-size:11px;line-height:13.5px;color:var(--text)}
.tier__lead b{font-weight:700;color:var(--ink)}
.tier__list{list-style:none;margin-top:3px}
.tier__list li{position:relative;padding-left:16px;font-size:11.2px;line-height:14px;color:var(--text);margin-bottom:7px}
.tier__list li::before{content:"";position:absolute;left:1px;top:3px;width:7px;height:7px;border:1px solid var(--text);border-radius:50%}
</style>
</head>
<body>
<div class="stage">

  <section class="page page--intro">
    <div class="abs hero"></div>
    <h1 class="abs hero__name">Meridian<br>Foundation</h1>
    <div class="abs hero__rule"></div>
    <h2 class="abs hero__program">Fiscal Sponsorship<br>Program</h2>

    <h3 class="abs section-title section-title--sm" style="left:55px;top:370px">Mission &amp; Vision</h3>
    <div class="abs" style="left:57px;top:415px;width:700px">
      <p class="para">The Meridian Foundation, founded in 2010, exists to support social impact campaigns and organizations through educational, public engagement, and awareness efforts.</p>
      <p class="para">Its vision is to strengthen the capacity of the social impact sector and its leaders by providing top-tier fiscal sponsorship services.</p>
    </div>

    <h3 class="abs section-title section-title--sm" style="left:55px;top:532px">What is Fiscal Sponsorship?</h3>
    <p class="abs para" style="left:54px;top:582px;width:365px">Fiscal sponsorship refers to the practice of non-profit organizations offering their legal and tax-exempt status to charitable projects or groups engaged in activities related to the sponsoring organization's mission. Fiscal sponsors provide oversight, financial management, and other administrative services to build the capacity of charitable projects.</p>
    <p class="abs subhead" style="left:54px;top:716px;width:365px">What kinds of projects are eligible for fiscal sponsorship?</p>
    <p class="abs para" style="left:54px;top:776px;width:365px">Meridian Foundation uses the following broad criteria to determine whether or not a project is eligible for fiscal sponsorship:</p>
    <ol class="abs criteria" style="left:54px;top:837px;width:372px">
      <li><span>1</span>Mission alignment with the Meridian Foundation.</li>
      <li><span>2</span>Whether or not the project provides an educational, social or charitable benefit.</li>
      <li><span>3</span>Whether or not the project's activities follow the IRS regulations governing 501(c)(3) public charities.</li>
    </ol>

    <aside class="abs philosophy">
      <h3 class="philosophy__title">Fiscal Sponsorship<br>Program<br>Philosophy</h3>
      <p>We believe we can accelerate the pace and scale of social change by providing strategic back office support to emerging projects, leaders and ideas.</p>
      <p>By providing light touch administrative and capacity building services, our fiscal sponsorship program takes the administrative burden off the shoulders of leaders and their projects toallow them to focus on what they do best - achieving impact and changing the world</p>
    </aside>

    <div class="abs contact" style="top:957px">
      <span class="contact__item">
        <svg width="18" height="18" viewBox="0 0 18 18" aria-hidden="true"><rect x="1" y="5" width="16" height="12" fill="#f45f5f"/><path d="M1 5 L9 11 L17 5" fill="none" stroke="#fff" stroke-width="1.4"/><rect x="5" y="1" width="8" height="5" fill="#f45f5f"/></svg>
        info@meridianfoundation.org
      </span>
      <span class="contact__item">
        <svg width="18" height="18" viewBox="0 0 18 18" aria-hidden="true"><circle cx="9" cy="9" r="8" fill="none" stroke="#f45f5f" stroke-width="1.8"/><ellipse cx="9" cy="9" rx="3.5" ry="8" fill="none" stroke="#f45f5f" stroke-width="1.4"/><path d="M1 9 H17 M2.5 5 H15.5 M2.5 13 H15.5" stroke="#f45f5f" stroke-width="1.4"/></svg>
        meridianfoundation.org
      </span>
    </div>
  </section>

  <section class="page page--details">
    <div class="abs values-band"></div>
    <h3 class="abs section-title section-title--lg section-title--light" style="left:55px;top:53px">Organizational Values</h3>

    <div class="abs value" style="left:54px;top:106px">
      <span class="value__icon"><svg width="22" height="22" viewBox="0 0 22 22" aria-hidden="true"><path d="M11 18 C4 13 3 9 5.5 6.5 C7.5 4.5 10 5.5 11 7.5 C12 5.5 14.5 4.5 16.5 6.5 C19 9 18 13 11 18Z" fill="#161616"/></svg></span>
      <div><p class="value__label">TRUST:</p><p class="value__text">We believe that all successful partnerships begin with a foundation of trust.</p></div>
    </div>
    <div class="abs value" style="left:54px;top:165px">
      <span class="value__icon"><svg width="22" height="22" viewBox="0 0 22 22" aria-hidden="true"><circle cx="11" cy="5" r="3" fill="#161616"/><path d="M3 16 L8 11 H14 L19 16 L16 18 L11 14 L6 18Z" fill="#161616"/></svg></span>
      <div><p class="value__label">RELATIONSHIPS:</p><p class="value__text">Our partners are central to our work. We honor our relationships through respect, communication and transparency.</p></div>
    </div>
    <div class="abs value" style="left:54px;top:235px">
      <span class="value__icon"><svg width="22" height="22" viewBox="0 0 22 22" aria-hidden="true"><path d="M11 3 L17 9 L11 15 L5 9Z" fill="#161616"/><rect x="4" y="16" width="14" height="3" fill="#161616"/></svg></span>
      <div><p class="value__label">EMBRACE COMPLEXITY AND RISK:</p><p class="value__text">We understand that bold solutions to intractable social issues often require both complexity and risk.</p></div>
    </div>
    <div class="abs value" style="left:428px;top:106px">
      <span class="value__icon"><svg width="22" height="22" viewBox="0 0 22 22" aria-hidden="true"><circle cx="11" cy="9" r="6" fill="#161616"/><rect x="8" y="15" width="6" height="4" fill="#161616"/></svg></span>
      <div><p class="value__label">INNOVATION:</p><p class="value__text">We embrace continuous improvement, bold creativity and change.</p></div>
    </div>
    <div class="abs value" style="left:428px;top:172px">
      <span class="value__icon"><svg width="22" height="22" viewBox="0 0 22 22" aria-hidden="true"><path d="M11 18 C4 13 3 9 5.5 6.5 C7.5 4.5 10 5.5 11 7.5 C12 5.5 14.5 4.5 16.5 6.5 C19 9 18 13 11 18Z" fill="#161616"/><circle cx="11" cy="11" r="2" fill="#fff"/></svg></span>
      <div><p class="value__label">DIVERSITY:</p><p class="value__text">We believe that all voices matter and that effective solutions are created when decision-making is inclusive across social, cultural and economic backgrounds.</p></div>
    </div>

    <h3 class="abs section-title section-title--commit" style="left:55px;top:336px">Meridian Foundation - Program Commitments</h3>

    <div class="abs commit-col" style="left:54px;top:400px;width:360px">
      <div class="commit">
        <svg class="commit__tick" width="14" height="14" viewBox="0 0 14 14" aria-hidden="true"><circle cx="7" cy="7" r="6" fill="none" stroke="#f45f5f"/><path d="M4 7 L6.2 9.2 L10 5" fill="none" stroke="#f45f5f" stroke-width="1.2"/></svg>
        <p class="commit__text">Fast, simple and efficient fiscal sponsorship program</p>
      </div>
      <div class="commit">
        <svg class="commit__tick" width="14" height="14" viewBox="0 0 14 14" aria-hidden="true"><circle cx="7" cy="7" r="6" fill="none" stroke="#f45f5f"/><path d="M4 7 L6.2 9.2 L10 5" fill="none" stroke="#f45f5f" stroke-width="1.2"/></svg>
        <p class="commit__text">Free and fast approval process -our application can be completed in 30 minutes or less. There is no fee to apply, and most projects can expect to receive a response on their application within 2 weeks</p>
      </div>
      <div class="commit">
        <svg class="commit__tick" width="14" height="14" viewBox="0 0 14 14" aria-hidden="true"><circle cx="7" cy="7" r="6" fill="none" stroke="#f45f5f"/><path d="M4 7 L6.2 9.2 L10 5" fill="none" stroke="#f45f5f" stroke-width="1.2"/></svg>
        <p class="commit__text">No fees and no minimums; projects of any size are welcome to apply</p>
      </div>
    </div>

    <div class="abs commit-col" style="left:425px;top:398px;width:335px">
      <div class="commit">
        <svg class="commit__tick" width="14" height="14" viewBox="0 0 14 14" aria-hidden="true"><circle cx="7" cy="7" r="6" fill="none" stroke="#f45f5f"/><path d="M4 7 L6.2 9.2 L10 5" fill="none" stroke="#f45f5f" stroke-width="1.2"/></svg>
        <p class="commit__text">Easy onboarding process</p>
      </div>
      <div class="commit">
        <svg class="commit__tick" width="14" height="14" viewBox="0 0 14 14" aria-hidden="true"><circle cx="7" cy="7" r="6" fill="none" stroke="#f45f5f"/><path d="M4 7 L6.2 9.2 L10 5" fill="none" stroke="#f45f5f" stroke-width="1.2"/></svg>
        <p class="commit__text">Dedicated customer service and customization of services, tailored to the individual sponsored project's needs</p>
      </div>
      <div class="commit">
        <svg class="commit__tick" width="14" height="14" viewBox="0 0 14 14" aria-hidden="true"><circle cx="7" cy="7" r="6" fill="none" stroke="#f45f5f"/><path d="M4 7 L6.2 9.2 L10 5" fill="none" stroke="#f45f5f" stroke-width="1.2"/></svg>
        <p class="commit__text">Complex, hybrid structures, partnerships and coalitions are strongly encouraged to apply</p>
      </div>
    </div>

    <div class="abs divider"></div>
    <h3 class="abs fee-title"><em>Fee</em> Structure</h3>

    <article class="abs tier" style="left:55px">
      <svg class="tier__banner" width="214" height="96" viewBox="0 0 214 96" aria-hidden="true"><polygon points="0,0 214,0 214,42 107,95 0,42" fill="#b3e5df"/><rect x="10" y="6" width="194" height="12" rx="6" fill="#c6ece6"/></svg>
      <h4 class="tier__name">BASIC<br>FEE - 4%</h4>
      <p class="tier__level">LIMITED</p>
      <div class="tier__body">
        <ul class="tier__list">
          <li>Project Fund Set-Up</li>
          <li>Administration and Management</li>
          <li>Financial Management</li>
          <li>Grant Proposal Review</li>
          <li>Grant Contract Review</li>
          <li>Project Reporting</li>
          <li>Insurance</li>
          <li>Annual Audit and Form 990</li>
        </ul>
      </div>
    </article>

    <article class="abs tier" style="left:290px;width:213px">
      <svg class="tier__banner" width="213" height="96" viewBox="0 0 213 96" aria-hidden="true"><polygon points="0,0 213,0 213,42 106.5,95 0,42" fill="#b3e5df"/><rect x="10" y="6" width="193" height="12" rx="6" fill="#c6ece6"/></svg>
      <h4 class="tier__name">STANDARD<br>FEE - 6%</h4>
      <p class="tier__level" style="left:24px">COMPREHENSIVE</p>
      <div class="tier__body" style="left:24px;width:186px">
        <p class="tier__lead"><b>Basic Services +</b></p>
        <ul class="tier__list" style="margin-top:8px">
          <li>Customized Financial Reporting</li>
          <li>Monthly Financial Statements</li>
          <li>Subgranting/regranting to U.S.based organizations</li>
          <li>Management of Vendor and Independent Contractors (1099s)</li>
        </ul>
      </div>
    </article>

    <article class="abs tier" style="left:519px;width:213px">
      <svg class="tier__banner" width="213" height="96" viewBox="0 0 213 96" aria-hidden="true"><polygon points="0,0 213,0 213,42 106.5,95 0,42" fill="#b3e5df"/><rect x="10" y="6" width="193" height="12" rx="6" fill="#c6ece6"/></svg>
      <h4 class="tier__name">CUSTOM<br>FEE - 10%</h4>
      <p class="tier__level" style="left:22px">CUSTOM</p>
      <div class="tier__body" style="left:22px;width:182px">
        <p class="tier__lead">Standard Services + custom services tailored to individual project needs.<br><b>Customization Options:</b></p>
        <ul class="tier__list">
          <li>Subgranting/regranting to international organizations</li>
          <li>Lobbying Filings</li>
          <li>Project Audit</li>
          <li>Grant Writing Assistance</li>
          <li>One-on-One Coaching</li>
        </ul>
      </div>
    </article>

    <div class="abs contact" style="top:972px">
      <span class="contact__item">
        <svg width="18" height="18" viewBox="0 0 18 18" aria-hidden="true"><rect x="1" y="5" width="16" height="12" fill="#f45f5f"/><path d="M1 5 L9 11 L17 5" fill="none" stroke="#fff" stroke-width="1.4"/><rect x="5" y="1" width="8" height="5" fill="#f45f5f"/></svg>
        info@meridianfoundation.org
      </span>
      <span class="contact__item">
        <svg width="18" height="18" viewBox="0 0 18 18" aria-hidden="true"><circle cx="9" cy="9" r="8" fill="none" stroke="#f45f5f" stroke-width="1.8"/><ellipse cx="9" cy="9" rx="3.5" ry="8" fill="none" stroke="#f45f5f" stroke-width="1.4"/><path d="M1 9 H17 M2.5 5 H15.5 M2.5 13 H15.5" stroke="#f45f5f" stroke-width="1.4"/></svg>
        meridianfoundation.org
      </span>
    </div>
  </section>

</div>
</body>
</html>
```